Beef cattle farm needs signs which can be seen from roadside

We would like submissions of artwork for a sign that will hang from a fence or gate and will be seen by passing cars.

Existing logo and branding theme for the company is attached.

Signage can be between 900mm x 400mm - 1200mm x 600mm

Industry/Entity Type

Farm

Requirements
Must have
• the Signs should have the following information:
• Company name: Brindle Ridge Grazing Company
• Address: 214 Wattlebank Hollow Road
• Contact number: 0431 862 475
• email address: admin@brindleridgegrazingco.com.au
• - Logo and branding as per attached artwork

```html
<!DOCTYPE html>
<html lang="en">
<head>
<meta charset="utf-8">
<title>Brindle Ridge Grazing Company – Roadside Sign</title>
<link href="https://fonts.googleapis.com/css2?family=Arimo:wght@400;700&display=swap" rel="stylesheet">
<style>
  :root {
    --backdrop: #e6e7e9;
    --sign: #ffffff;
    --edge: #9a9a9a;
    --green: #145c36;
  }
  html, body {
    margin: 0;
    padding: 0;
    width: 1200px;
    height: 1191px;
    overflow: hidden;
    background: var(--backdrop);
  }
  .canvas {
    position: relative;
    width: 1200px;
    height: 1191px;
    font-family: "Arimo", Arial, sans-serif;
    color: var(--green);
  }
  .sign {
    position: absolute;
    left: 32px;
    top: 291px;
    width: 1136px;
    height: 567px;
    background: var(--sign);
    border: 1px solid var(--edge);
    box-sizing: border-box;
  }
  .address {
    position: absolute;
    left: 0;
    right: 0;
    top: 356px;
    margin: 0;
    text-align: center;
    font-weight: 700;
    font-size: 58px;
    letter-spacing: 1.5px;
    line-height: 1;
  }
  .brand {
    position: absolute;
    top: 456px;
    width: 230px;
    text-align: center;
  }
  .brand--left { left: 80px; }
  .brand--right { left: 888px; }
  .brand__dot {
    display: block;
    width: 146px;
    height: 146px;
    margin: 0 auto 12px;
    border-radius: 50%;
    background: var(--green);
  }
  .brand__name {
    margin: 0;
    font-weight: 700;
    font-size: 22px;
    line-height: 1.15;
    text-transform: uppercase;
    white-space: nowrap;
  }
  .phone {
    position: absolute;
    left: 621px;
    top: 568px;
    margin: 0;
    transform: translate(-50%, -50%) rotate(-26deg);
    font-weight: 700;
    font-size: 76px;
    letter-spacing: 3px;
    white-space: nowrap;
    line-height: 1;
  }
  .email {
    position: absolute;
    left: 0;
    right: 0;
    top: 726px;
    margin: 0;
    text-align: center;
    font-weight: 400;
    font-size: 56px;
    letter-spacing: 1.5px;
    line-height: 1;
    white-space: nowrap;
  }
</style>
</head>
<body>
<main class="canvas">
  <div class="sign"></div>

  <h1 class="address">214 WATTLEBANK HOLLOW ROAD</h1>

  <div class="brand brand--left">
    <span class="brand__dot"></span>
    <p class="brand__name">Brindle Ridge<br>Grazing Company</p>
  </div>

  <div class="brand brand--right">
    <span class="brand__dot"></span>
    <p class="brand__name">Brindle Ridge<br>Grazing Company</p>
  </div>

  <p class="phone">0431 862 475</p>

  <p class="email">admin@brindleridgegrazingco.com.au</p>
</main>
</body>
</html>
```